Thornbury Lettings Managment Ltd website

Need a website To inform people/clients of the services we provide. 5 pages total with a local feel. Bristol, UK. I have logo artwork already is like the look based on
incorporate the artwork attached for theme, feel and colours fonts info etc

To best describe the business have a brief look at www.fernwickhomes.example.co.uk which is a local firm offering the same services. This is for your ref only and not to be copied.

Target Market(s)

Property Investors/Landlords

Coding

Coded - Design and coding required

Number of Pages Required

5+ page

Colors
0392cd
f68d4d

Requirements
Must have
• local feel. Possibly using some local architecture or historic landmarks etc. This is fexible.
• most also be mobile device compatible
Nice to have
• the membership logos - files attached: KTB, DWF, GMV and safehold-example.co.uk

```html
<!DOCTYPE html>
<html lang="en">
<head>
<meta charset="utf-8">
<title>Thornbury Lettings Managment Ltd</title>
<link href="https://fonts.googleapis.com/css2?family=Arimo:ital,wght@0,400;0,700;1,400&display=swap" rel="stylesheet">
<style>
:root{
  --teal:#2a7390;
  --teal-dark:#23627b;
  --orange:#f68d4d;
  --text:#555;
  --text-dark:#333;
  --page:#e8e8e8;
  --band:#f4f4f4;
  --line:#c9c9c9;
  --footer:#4d4d4d;
}
*{box-sizing:border-box;margin:0;padding:0}
html,body{width:1200px;height:1200px;overflow:hidden}
body{position:relative;background:linear-gradient(#ececec,#e4e4e4);font-family:"Arimo",Arial,sans-serif;color:var(--text)}
.abs{position:absolute}
.top-rule{left:0;top:0;width:1200px;height:3px;background:#555}

.brand{left:122px;top:32px;display:flex;align-items:center;gap:12px}
.brand-mark{width:22px;height:22px;background:var(--teal)}
.brand-name{font-size:24px;font-weight:700;color:var(--teal);line-height:1.1}
.brand-sub{font-size:12px;font-weight:700;color:var(--teal);letter-spacing:.3px}

.callback-note{left:799px;top:25px;font-size:12px;line-height:14px;color:#444}
.callback{left:793px;top:60px;width:285px;height:43px;border-radius:8px;background:linear-gradient(#f6f6f6,#d6d6d6);box-shadow:0 1px 2px rgba(0,0,0,.35);display:flex;align-items:center;padding-left:12px}
.callback .field{height:20px;border-radius:10px;background:#e3e3e3;box-shadow:inset 0 1px 2px rgba(0,0,0,.35)}
.callback .dash{margin:0 5px;font-size:12px}
.callback .call{position:absolute;right:0;top:0;width:46px;height:43px;border-left:1px solid #bbb;display:flex;align-items:center;justify-content:center}

.nav{left:120px;top:117px;display:flex;align-items:center;font-size:14px}
.nav a{color:var(--teal);text-decoration:none;margin-right:39px}
.nav a.current{color:var(--orange);width:62px;height:31px;line-height:30px;text-align:center;border-radius:7px;background:linear-gradient(#f8f8f8,#dedede);box-shadow:0 1px 2px rgba(0,0,0,.4);margin-right:28px}

.hero{left:0;top:193px;width:1200px;height:332px;background:linear-gradient(90deg,#6b5d86 0%,#a27d7a 15%,#cfc1a8 40%,#8f8a79 55%,#5a6478 80%,#3e4a66 100%)}
.hero-caption{left:518px;top:210px;width:682px;height:110px;background:rgba(30,30,30,.62);padding:10px 20px;color:#fff}
.hero-caption h1{font-size:30px;font-weight:400;margin-bottom:10px;letter-spacing:-.3px}
.hero-caption p{font-size:13.5px;line-height:18px}
.slider-tab{left:505px;top:490px;width:210px;height:35px;background:#3a3a3a;clip-path:polygon(8% 0,92% 0,100% 100%,0 100%)}
.dots{left:561px;top:501px;display:flex;gap:13px}
.dots span{width:13px;height:13px;border-radius:50%;background:#222;box-shadow:0 1px 0 rgba(255,255,255,.2)}
.dots span.on{background:var(--orange)}

.support-tab{left:0;top:505px;width:60px;height:170px;background:linear-gradient(90deg,#dcdcdc,#f2f2f2);border-radius:0 6px 6px 0;box-shadow:1px 1px 3px rgba(0,0,0,.35);z-index:2}
.support-tab div{position:absolute;left:30px;top:85px;transform:translate(-50%,-50%) rotate(-90deg);white-space:nowrap;text-align:center;font-size:13px;line-height:16px;color:#555}
.support-tab b{display:block;font-size:14px;color:#333}

.members{left:0;top:525px;width:1200px;height:131px;background:var(--band);border-bottom:1px solid var(--line)}
.members h2{position:absolute;left:128px;top:35px;font-size:30px;font-weight:400;color:var(--teal);letter-spacing:-.3px}
.members p{position:absolute;left:128px;top:72px;font-size:15.5px;color:#333}
.badge{position:absolute;background:#c9c9c9}
.chev{position:absolute;left:1050px;top:53px}

.col h3{font-size:20px;font-weight:400;color:#444;padding-bottom:10px;border-bottom:1px solid var(--line);width:291px}
.col h3 span{color:var(--teal)}
.col .photo{margin-top:17px;width:292px;height:127px;border:1px solid #bbb;background:#fff;padding:4px}
.col .photo div{width:100%;height:100%}
.col p{margin-top:13px;width:291px;font-size:12.3px;line-height:18px;text-align:justify;color:#555}
.more{margin-top:6px;display:inline-flex;align-items:center;height:20px;border-radius:10px;background:linear-gradient(#fafafa,#dcdcdc);box-shadow:0 1px 2px rgba(0,0,0,.4);font-size:10px;color:#444}
.more span{padding:0 6px 0 8px;border-right:1px solid #bbb;line-height:14px}
.more i{width:16px;display:flex;justify-content:center}

.form h3{width:291px}
.input{position:absolute;height:32px;border-radius:8px;background:linear-gradient(#d3d3d3,#e6e6e6);box-shadow:inset 0 1px 2px rgba(0,0,0,.25),0 1px 0 #fff;font-size:12px;font-style:italic;color:#555;padding:10px 19px}
.submit{position:absolute;left:770px;top:969px;width:140px;height:36px;border-radius:7px;background:linear-gradient(#fafafa,#d8d8d8);box-shadow:0 1px 2px rgba(0,0,0,.4);font-size:14px;color:#333;text-align:center;line-height:36px}

.footer{left:0;top:1155px;width:1200px;height:45px;background:linear-gradient(#5a5a5a,#444);color:#fff;font-size:12.5px;text-align:center;line-height:44px}
.footer span{margin:0 12px}
</style>
</head>
<body>
<div class="abs top-rule"></div>

<div class="abs brand">
  <div class="brand-mark"></div>
  <div>
    <div class="brand-name">Thornbury</div>
    <div class="brand-sub">lettings management ltd</div>
  </div>
</div>

<div class="abs callback-note">Enter your number and we will call you<br>to anwer any questions</div>
<div class="abs callback">
  <div class="field" style="width:62px"></div>
  <div class="field" style="width:62px;margin-left:3px"></div>
  <span class="dash">-</span>
  <div class="field" style="width:73px"></div>
  <div class="call">
    <svg width="26" height="22" viewBox="0 0 26 22"><path d="M2 8c0-4 5-6 11-6s11 2 11 6v2h-6V7H8v3H2z" fill="#333"/><path d="M7 10h12l4 10H3z" fill="#333"/><circle cx="13" cy="15" r="3" fill="#ddd"/></svg>
  </div>
</div>

<nav class="abs nav">
  <a class="current" href="#">Home</a>
  <a href="#">Landlords</a>
  <a href="#">Agencies</a>
  <a href="#">Properties</a>
  <a href="#">About Us</a>
  <a href="#">Contact Us</a>
</nav>

<div class="abs hero" role="img" aria-label="Photo of a modern glass office building at dusk"></div>
<div class="abs hero-caption">
  <h1>Find a home.</h1>
  <p>Whether you're looking to buy or rent your new home, we have you covered.<br>Let us help you find your dream home today.</p>
</div>
<div class="abs slider-tab"></div>
<div class="abs dots"><span class="on"></span><span></span><span></span><span></span></div>

<div class="abs support-tab"><div>Sales &amp; Support<b>OFLLINE</b></div></div>

<section class="abs members">
  <h2>Membership</h2>
  <p>The perfect solution for landlord.</p>
  <div class="badge" style="left:432px;top:50px;width:138px;height:36px"></div>
  <div class="badge" style="left:615px;top:37px;width:46px;height:60px"></div>
  <div class="badge" style="left:713px;top:57px;width:147px;height:22px;background:#9ccfd8"></div>
  <div class="badge" style="left:910px;top:40px;width:86px;height:55px"></div>
  <svg class="chev" width="20" height="28" viewBox="0 0 20 28"><path d="M4 3l11 11L4 25" fill="none" stroke="#bbb" stroke-width="4"/></svg>
</section>

<div class="abs col" style="left:129px;top:682px">
  <h3><span>Committed</span> to Our Clients</h3>
  <div class="photo"><div role="img" aria-label="Photo of two businessmen in a meeting" style="background:linear-gradient(90deg,#3c3a38,#7a7166,#2b2a2a)"></div></div>
  <p>Lorem ipsum dolor sit amet, consectetur adipiscing elit. Phasellus posuere neque ut massa scelerisque eu imperdiet purus pellentesque. Aenean nisl turpis, euismod vitae malesuada ac, sagittis sed.</p>
  <div class="more"><span>Read More</span><i><svg width="5" height="7"><path d="M0 0l5 3.5L0 7z" fill="#444"/></svg></i></div>
</div>

<div class="abs col" style="left:449px;top:682px">
  <h3><span>Solutions</span> for the Tenants</h3>
  <div class="photo"><div role="img" aria-label="Photo of business people assembling large white puzzle pieces" style="background:linear-gradient(90deg,#e6e6e6,#c8c8c8,#f0f0f0)"></div></div>
  <p>Lorem ipsum dolor sit amet, consectetur adipiscing elit. Phasellus posuere neque ut massa scelerisque eu imperdiet purus pellentesque. Aenean nisl turpis, euismod vitae malesuada ac, sagittis sed erat. Suspendisse malesuada est sed purus consectetur.</p>
  <div class="more"><span>Read More</span><i><svg width="5" height="7"><path d="M0 0l5 3.5L0 7z" fill="#444"/></svg></i></div>
</div>

<div class="abs col form" style="left:768px;top:682px">
  <h3><span>How</span> Can We Help You?</h3>
</div>
<div class="input" style="left:770px;top:732px;width:150px">First Name...</div>
<div class="input" style="left:930px;top:732px;width:150px">Last Name...</div>
<div class="input" style="left:770px;top:768px;width:310px">Company...</div>
<div class="input" style="left:770px;top:804px;width:310px">E-mail Address...</div>
<div class="input" style="left:770px;top:839px;width:310px">Phone Number...</div>
<div class="input" style="left:770px;top:877px;width:310px;height:77px;padding-top:14px">What can we help with?</div>
<div class="submit">Submit</div>

<footer class="abs footer">
  Copyright 2016 BRIGHTLANE<span>|</span>About Us<span>|</span>Contact Us<span>|</span>Privacy Policy<span>|</span>Terms of Use
</footer>
</body>
</html>
```